The Maple Sprout Clinic needs a Letterhead

We are a bilingual pediatric clinic located in Montreal, Canada.

Our english name is Maple Sprout Clinic
Our french name is Clinique du petit ruisseau

We offer complete care for children including general pediatric care, pediatric specialist care such as Ear, Nose and Throat, Urology, Neurology and Adolescent Medicine. We also have paramedical specialists such as psychologists, social workers, occupational therapists, speech and language pathologists.

The letterhead must use and be harmonious with our new logo. See Design #4923293. We need two types of letterhead. One for a the Logo and both english and french names on the top and the second with the list of current staff on the left. I have uploaded two old examples for you to see. Thanks and good luck.

Font styles to use
Sans Serif

Colors
3176b5
9d9d9d

Requirements
Must have
• Include our logo.
Nice to have
• Most of our printing is done in black and white. So a grayscale design is fine.
I have included a color and grayscale versions of our logo.

We prefer clean modern designs.

```html
<!DOCTYPE html>
<html lang="fr">
<head>
<meta charset="utf-8">
<title>Maple Sprout Clinic – Letterhead</title>
<link rel="stylesheet" href="https://fonts.googleapis.com/css2?family=Arimo:wght@400&display=swap">
<style>
  :root {
    --backdrop: #1f1f1f;
    --paper: #ffffff;
    --paper-edge: #3a3a3a;
    --ink: #1a1a1a;
    --brand-grey: #8a8a8a;
    --band-grey: #d4d4d4;
    --band-light: #ececec;
    --rule-dark: #5a5a5a;
  }
  * { margin: 0; padding: 0; box-sizing: border-box; }
  html, body { width: 1200px; height: 900px; overflow: hidden; }
  body {
    background: var(--backdrop);
    font-family: "Arimo", Arial, sans-serif;
    color: var(--ink);
    position: relative;
  }
  .sheet {
    position: absolute;
    top: 71px;
    width: 524px;
    height: 742px;
    background: var(--paper);
    border: 1px solid var(--paper-edge);
  }
  .sheet--staff { left: 56px; }
  .sheet--plain { left: 610px; }

  .side-band {
    position: absolute;
    top: 0;
    left: 9px;
    width: 42px;
    height: 742px;
  }
  .sheet--staff .side-band {
    background: linear-gradient(90deg, var(--band-grey), #e2e2e2);
    height: 714px;
  }
  .sheet--plain .side-band {
    width: 40px;
    background: linear-gradient(180deg, var(--band-grey), var(--band-light) 80%, #f6f6f6);
  }

  .staff-list {
    position: absolute;
    top: 20px;
    left: 10px;
    font-size: 10.4px;
    line-height: 12.6px;
  }
  .staff-group { margin-bottom: 12.6px; }

  .brand {
    position: absolute;
    top: 20px;
    right: 12px;
    display: flex;
    align-items: center;
    gap: 4px;
    color: var(--brand-grey);
    font-size: 12.5px;
    line-height: 14px;
  }
  .brand-fr { text-align: right; }
  .brand-en { text-align: left; }
  .brand-dot {
    width: 48px;
    height: 48px;
    border-radius: 50%;
    border: 6px solid var(--brand-grey);
  }

  .footer {
    position: absolute;
    right: 10px;
    bottom: 11px;
    text-align: right;
    font-size: 10.4px;
    line-height: 13px;
  }
  .footer-rule {
    position: absolute;
    left: 0;
    bottom: 15px;
    width: 330px;
    height: 3px;
    background: linear-gradient(90deg, var(--rule-dark), #9a9a9a 70%, #d8d8d8);
  }
</style>
</head>
<body>

  <section class="sheet sheet--staff">
    <div class="side-band"></div>

    <div class="staff-list">
      <div class="staff-group">
        Addresse / Address<br>
        2250 boul. des Érables<br>
        Suite 100<br>
        Rivière-Verte, Qc<br>
        H0H 2B3<br>
        Tél. (514) 555-0142<br>
        Fax. (514) 555-0199
      </div>
      <div class="staff-group">
        Pédiatres / Pediatricians<br>
        H. Larose<br>
        J. Bellamy<br>
        R. Tremblay<br>
        D. Fontaine<br>
        N. Gagnon<br>
        M.Caron<br>
        D.Morin
      </div>
      <div class="staff-group">Neurologue / Neurologist<br>M. Pelletier</div>
      <div class="staff-group">O.R.L. / E.N.T.<br>T. Lavoie</div>
      <div class="staff-group">Urologue / Urologist<br>R. Beaulieu</div>
      <div class="staff-group">Psychologues / Psychologists<br>H. Dubois<br>A. Girard</div>
      <div class="staff-group">Travailleuse social<br>/ Social worker<br>S. Roy</div>
      <div class="staff-group">Dietetiste / Dietician<br>L. Bouchard</div>
      <div class="staff-group">Gerante / Manager<br>C.Lefebvre</div>
    </div>

    <div class="brand">
      <div class="brand-fr">Clinique du<br>petit<br>ruisseau</div>
      <div class="brand-dot"></div>
      <div class="brand-en">Maple<br>Sprout<br>Clinic</div>
    </div>

    <div class="footer-rule"></div>
    <div class="footer">
      2250 boul. des Érables, Suite 100, Rivière-Verte, Qc, H0H 2B3<br>
      tél (514) 555-0142 fax (514) 555-0199
    </div>
  </section>

  <section class="sheet sheet--plain">
    <div class="side-band" role="img" aria-label="Faint vertical band repeating the clinic name"></div>

    <div class="brand">
      <div class="brand-fr">Clinique du<br>petit<br>ruisseau</div>
      <div class="brand-dot"></div>
      <div class="brand-en">Maple<br>Sprout<br>Clinic</div>
    </div>

    <div class="footer-rule"></div>
    <div class="footer">
      2250 boul. des Érables, Suite 100, Rivière-Verte, Qc, H0H 2B3<br>
      tél (514) 555-0142 fax (514) 555-0199
    </div>
  </section>

</body>
</html>
```